Business Card Design for Varnel

I've already got the logo, but I'd like to see some interesting designs.

I don't want anything to complex. I like it simple,yet innovative, like the logo.

My business is System Administration for small to medium size businesses, so that will be my main target audience.
Updates

hey all, the png has been uploaded.

Hey all,

If you are submitting the back side of the card, I'd like the top bit of the card to be Varnel Solutions and the logo, the bottom of the card the website, with a white background.

The middle I'd like to leave blank for a quote that will be printed on each card.

Thanks!

Doug

Industry/Entity Type

Business

```html
<!DOCTYPE html>
<html lang="en">
<head>
<meta charset="utf-8">
<title>Varnel Solutions – Business Card</title>
<link rel="stylesheet" href="https://fonts.googleapis.com/css2?family=Arimo:wght@400;500&family=Oswald:wght@600&display=swap">
<style>
  :root {
    --board: #2c2c2c;
    --accent: #f7931e;
    --frame: #d9801f;
    --card: #ffffff;
    --band: #e8e8e8;
    --rule: #2a74b0;
    --brand: #2a7fc1;
    --ink: #333333;
    --ink-soft: #555555;
    --icon: #444444;
  }
  * { box-sizing: border-box; margin: 0; padding: 0; }
  html, body { width: 1200px; height: 1000px; overflow: hidden; }
  body {
    position: relative;
    background: radial-gradient(ellipse at 50% 40%, #343434 0%, var(--board) 70%);
    font-family: "Arimo", Arial, sans-serif;
  }
  .frame { position: absolute; border: 1px solid var(--frame); }
  .frame--front { left: 55px; top: 55px; width: 724px; height: 444px; }
  .frame--back { left: 415px; top: 498px; width: 724px; height: 444px; }
  .corner { position: absolute; background: var(--frame); }
  .side-label {
    position: absolute;
    font-family: "Oswald", "Arial Narrow", sans-serif;
    font-weight: 600;
    font-size: 58px;
    color: var(--accent);
    line-height: 1;
  }
  .card { position: absolute; background: var(--card); overflow: hidden; }
  .card--front { left: 67px; top: 67px; width: 698px; height: 419px; }
  .card--back { left: 428px; top: 511px; width: 698px; height: 417px; }

  .side-art {
    position: absolute; left: 0; top: 0; width: 300px; height: 419px;
    background: linear-gradient(to right, #8e8e8e 0%, #bdbdbd 35%, #e6e6e6 65%, rgba(255,255,255,0) 100%);
  }
  .header-band { position: absolute; left: 18px; top: 48px; right: 0; height: 107px; background: var(--band); border-bottom: 2px solid var(--rule); }
  .brand { position: absolute; display: flex; align-items: center; gap: 14px; }
  .brand__mark { width: 60px; height: 60px; border-radius: 50%; background: var(--brand); flex: none; }
  .brand__name { font-family: "Arimo", Arial, sans-serif; font-weight: 500; font-size: 33px; color: var(--brand); letter-spacing: -0.5px; white-space: nowrap; }
  .card--front .brand { left: 62px; top: 70px; }

  .person { position: absolute; right: 73px; top: 70px; text-align: right; }
  .person__name { font-family: "Oswald", "Arial Narrow", sans-serif; font-weight: 600; font-size: 34px; color: #2a2a2a; line-height: 1; letter-spacing: 0.3px; }
  .person__role { font-size: 20px; color: var(--brand); margin-top: 4px; }

  .contact { position: absolute; right: 111px; font-size: 20px; color: var(--ink); letter-spacing: 1.4px; text-align: right; line-height: 24px; }
  .contact--phone { top: 230px; }
  .contact--email { top: 283px; }
  .contact--address { top: 335px; }
  .email-band { position: absolute; left: 122px; right: 0; top: 268px; height: 52px; background: var(--band); border-top: 1px solid #c9c9c9; }
  .icon { position: absolute; right: 70px; }

  .back-top { position: absolute; left: 0; top: 0; right: 0; height: 134px; background: var(--band); border-bottom: 2px solid var(--rule); }
  .card--back .brand { left: 50%; top: 37px; transform: translateX(-50%); }
  .quote-space { position: absolute; left: 0; right: 0; top: 136px; height: 218px; }
  .back-bottom { position: absolute; left: 0; right: 0; bottom: 0; height: 63px; background: var(--band); display: flex; align-items: center; justify-content: center; font-size: 22px; letter-spacing: 0.3px; color: var(--ink-soft); }
</style>
</head>
<body>
  <div class="frame frame--front"></div>
  <div class="frame frame--back"></div>
  <div class="corner" style="left:870px;top:56px;width:269px;height:1px"></div>
  <div class="corner" style="left:1138px;top:56px;width:1px;height:272px"></div>
  <div class="corner" style="left:56px;top:668px;width:1px;height:272px"></div>
  <div class="corner" style="left:56px;top:940px;width:269px;height:1px"></div>

  <div class="side-label" style="left:963px;top:112px">Front</div>
  <div class="side-label" style="left:107px;top:836px">Back</div>

  <section class="card card--front">
    <div class="side-art" role="img" aria-label="Decorative grey flowing curves along the left edge"></div>

    <div class="header-band"></div>
    <div class="brand">
      <span class="brand__mark"></span>
      <span class="brand__name">Varnel Solutions</span>
    </div>
    <div class="person">
      <div class="person__name">Doug Harlow</div>
      <div class="person__role">Director</div>
    </div>

    <div class="contact contact--phone">123-456-7890</div>
    <svg class="icon" style="top:226px" width="20" height="30" viewBox="0 0 20 30" aria-hidden="true">
      <rect x="1.5" y="1.5" width="17" height="27" rx="2" fill="none" stroke="var(--icon)" stroke-width="1.6"/>
      <rect x="4.5" y="5" width="11" height="11" fill="var(--icon)"/>
      <rect x="4.5" y="19" width="11" height="6" fill="var(--icon)"/>
    </svg>

    <div class="email-band"></div>
    <div class="contact contact--email">doug@varnelsolutions.com</div>
    <svg class="icon" style="top:285px" width="28" height="20" viewBox="0 0 28 20" aria-hidden="true">
      <rect x="1" y="1" width="26" height="18" fill="none" stroke="var(--icon)" stroke-width="1.4"/>
      <path d="M1 1 L14 11 L27 1 M1 19 L11 9 M27 19 L17 9" fill="none" stroke="var(--icon)" stroke-width="1.4"/>
    </svg>

    <div class="contact contact--address">4120 Harbor Road River<br>MA 02719</div>
    <svg class="icon" style="top:343px" width="28" height="28" viewBox="0 0 28 28" aria-hidden="true">
      <path d="M2 13 L14 3 L26 13" fill="none" stroke="var(--icon)" stroke-width="1.6"/>
      <rect x="5" y="12" width="18" height="14" fill="none" stroke="var(--icon)" stroke-width="1.6"/>
      <rect x="8" y="15" width="5" height="5" fill="var(--icon)"/>
      <rect x="16" y="16" width="4" height="10" fill="var(--icon)"/>
    </svg>
  </section>

  <section class="card card--back">
    <div class="back-top"></div>
    <div class="brand">
      <span class="brand__mark"></span>
      <span class="brand__name">Varnel Solutions</span>
    </div>
    <div class="quote-space"></div>
    <div class="back-bottom">www.varnelsolutions.com</div>
  </section>
</body>
</html>
```